Business Cards for our company

Hi there,

we have successfully designed a logo with ArtFlock and would like now to design our business cards. We would like to keep the colours and the look-and-feel of the logo. Please send in variations with two or three colours and one or two sides. I promise to respond to every single submission.

Many thanks and happy new year.

All the best,
Wilfried

Target Market(s)

B2B

Industry/Entity Type

Trade

Contact Information for Business Card

We have successfully designed a logo with ArtFlock and would like now to design our business cards. We would like to keep the colours and the look-and-feel of the logo. Please send in variations with two or three colours and one or two sides. I promise to respond to every single submission.

Font styles to use
Serif
Sans Serif
Script

Requirements
Must have
• These information should be on the business card, grouped as you suggest, and we think using small pictograms for mobile, email, etc is pretty helpful:
• Wilfried Tammler (first and second name)
• Geschäftsführer/ Managing Director (title)
• KoR Warenkontor GmbH (company name and legal form)
• Ostheimer Str. 18/3 (street and house number)
• 41267 Haldenbach (zip code and town)
• +491629384562 (mobile)
• +4962419027341 (work)
• w.tammler@marlowfinch.example (email)
• www.marlowfinch.example (web)
Nice to have
• Spectacular and interesting layout and design. You look at it and think, wow, that's not the normal stuff.
• We think of ourselves as bridge-builders between businesses (international producers on the one hand, and retail chains on the other hand) and we translate, organise and manage projects where both partners are involved, but it's difficult for them to cooperate due to language barriers and different working cultures.
• This is why we have the n between the B's shaped as a bridge, and the green arc supports this idea. Maybe you could play with this idea...
Should not have
• the standard layout that everybody has

```html
<!DOCTYPE html>
<html lang="en">
<head>
<meta charset="utf-8">
<title>Marlow Finch – Business Card</title>
<link rel="stylesheet" href="https://fonts.googleapis.com/css2?family=Lato:ital,wght@0,400;0,700;0,900;1,900&display=swap">
<style>
  :root {
    --backdrop: #d9d4cc;
    --card-black: #141515;
    --lime: #a6d33a;
    --white: #f4f4f4;
    --grey: #9a9a9a;
    --logo-panel: #ececec;
    --logo-ink: #2a2a2a;
  }
  html, body {
    margin: 0;
    padding: 0;
    width: 1200px;
    height: 900px;
    overflow: hidden;
    background: var(--backdrop);
    font-family: "Lato", Arial, sans-serif;
  }
  .card {
    position: absolute;
    left: 110px;
    top: 170px;
    width: 980px;
    height: 560px;
    background: var(--card-black);
    box-shadow: 0 18px 40px rgba(0,0,0,0.25);
  }
  .logo-panel {
    position: absolute;
    left: 610px;
    top: 34px;
    width: 350px;
    height: 76px;
    background: var(--logo-panel);
    display: flex;
    align-items: center;
    justify-content: center;
  }
  .logo-name {
    font-weight: 900;
    font-size: 34px;
    color: var(--logo-ink);
    letter-spacing: 0.5px;
  }
  .logo-bar {
    position: absolute;
    left: 585px;
    top: 114px;
    width: 375px;
    height: 9px;
    background: var(--lime);
  }
  .person {
    position: absolute;
    left: 150px;
    top: 162px;
  }
  .person-name {
    margin: 0;
    font-weight: 900;
    font-style: italic;
    font-size: 25px;
    color: var(--lime);
    text-transform: uppercase;
    letter-spacing: 0.3px;
  }
  .person-title {
    margin: 2px 0 0;
    font-size: 19px;
    color: var(--grey);
    text-transform: uppercase;
  }
  .address {
    position: absolute;
    left: 108px;
    top: 250px;
  }
  .label {
    margin: 0 0 8px;
    font-weight: 900;
    font-size: 20px;
    color: var(--lime);
    text-transform: uppercase;
    letter-spacing: 0.5px;
  }
  .line {
    margin: 0;
    font-size: 21px;
    line-height: 1.45;
    color: var(--grey);
  }
  .contact {
    position: absolute;
    right: 30px;
    text-align: right;
  }
  .contact .line { color: var(--white); font-size: 22px; }
  .contact-phone { top: 190px; }
  .contact-web { top: 322px; }
</style>
</head>
<body>
  <div class="card">
    <div class="logo-panel"><span class="logo-name">Marlow Finch</span></div>
    <div class="logo-bar"></div>

    <div class="person">
      <p class="person-name">Wilfried Tammler</p>
      <p class="person-title">Managing Director</p>
    </div>

    <div class="address">
      <p class="label">Addrees</p>
      <p class="line">18/3,Ostheimer Str.</p>
      <p class="line">41267 Haldenbach</p>
    </div>

    <div class="contact contact-phone">
      <p class="label">Phone &amp; Mobile</p>
      <p class="line">+491629384562</p>
      <p class="line">+4962419027341</p>
    </div>

    <div class="contact contact-web">
      <p class="label">Web &amp; Email</p>
      <p class="line">w.tammler@marlowfinch.example</p>
      <p class="line">www.marlowfinch.example</p>
    </div>
  </div>
</body>
</html>
```